Flyer for Consulting Services (PM+Dev-Lead)

• The attached document describes consulting services for StartUps or young companies with a digital buisness model. We provide services for product management and development lead/scrum master. The target group of the flyer (i.e. who reads that flyer) is CEOs of Startups, Founders, Investors, Business Angle.s
• The task is to design an A4 flyer with one page layout (one pager) mostly for electronic destribution (printing second choice). There have to be two versions according given input: one in German and one in English with same layout. Preferably a format which allows us to adjust wording (e.g. Word, MS Publisher, …)
The final design should deliver professionality on one side and agility/StartUp mentality on the other side.

```html
<!DOCTYPE html>
<html lang="en">
<head>
<meta charset="utf-8">
<title>Product Management &amp; Development Partner – Flyer</title>
<link href="https://fonts.googleapis.com/css2?family=Bebas+Neue&family=Source+Sans+3:wght@400;600;700&display=swap" rel="stylesheet">
<style>
  :root {
    --blue: #1a9ad6;
    --blue-dark: #0d6fa8;
    --dark: #2e2e30;
    --dark-band: #3a3a3c;
    --light: #f2f2f2;
    --ink: #1c1c1c;
    --text-light: #ffffff;
    --muted: #4a4a4a;
    --rule: #c8c8c8;
  }
  * { margin: 0; padding: 0; box-sizing: border-box; }
  html, body { width: 946px; height: 1200px; overflow: hidden; background: #e6e6e6; }
  body { font-family: "Source Sans 3", Arial, sans-serif; }

  .flyer { position: relative; width: 946px; height: 1200px; background: var(--light); overflow: hidden; }

  .hero {
    position: absolute; left: 0; top: 0; width: 946px; height: 433px;
    background: linear-gradient(180deg, #6f767c 0%, #8b9196 35%, #5a5450 70%, #3d3631 100%);
  }
  .hero-title {
    position: absolute; left: 0; top: 22px; width: 946px; text-align: center;
    font-family: "Bebas Neue", Impact, sans-serif; font-size: 47px; line-height: 43px;
    letter-spacing: 1.5px; color: var(--text-light);
  }

  .you { position: absolute; left: 30px; top: 464px; width: 440px; }
  .you-heading { font-family: "Bebas Neue", Impact, sans-serif; font-size: 68px; line-height: 64px; color: #111; }
  .question { position: absolute; left: 0; display: flex; align-items: center; }
  .question-icon { width: 84px; height: 88px; flex: none; }
  .question-text { margin-left: 23px; font-size: 26px; line-height: 26px; color: var(--ink); }

  .contact { position: absolute; left: 20px; top: 874px; width: 420px; border-top: 1px solid var(--rule); }
  .contact-heading { margin-top: 24px; font-size: 18px; font-weight: 700; letter-spacing: 1.2px; color: #111; }
  .person { margin-top: 18px; margin-left: 6px; font-size: 15px; line-height: 20px; color: var(--muted); }
  .person + .person { margin-top: 10px; }
  .person-line { display: flex; align-items: center; }
  .person-line svg { width: 12px; height: 12px; margin-right: 8px; flex: none; }

  .site-band {
    position: absolute; left: 0; top: 1135px; width: 474px; height: 65px;
    background: var(--dark-band); display: flex; align-items: center; padding-left: 27px;
  }
  .site-url { font-size: 20px; font-weight: 600; letter-spacing: 2.4px; color: var(--blue); }

  .offer { position: absolute; left: 474px; top: 433px; width: 472px; height: 767px; background: var(--dark); }
  .section-head {
    position: absolute; left: 471px; width: 475px; height: 55px; background: var(--blue);
    color: var(--text-light); font-size: 26px; line-height: 55px; padding-left: 20px;
  }
  .section-head::after {
    content: ""; position: absolute; left: 28px; bottom: -8px;
    border-left: 10px solid transparent; border-right: 10px solid transparent; border-top: 8px solid var(--blue);
  }
  .item {
    position: absolute; left: 494px; width: 445px; padding-left: 24px;
    font-size: 15px; line-height: 15px; color: var(--text-light);
  }
  .item svg { position: absolute; left: 0; top: 1px; width: 15px; height: 15px; }
</style>
</head>
<body>
<main class="flyer">

  <section class="hero" role="img" aria-label="Photo of six young people sitting together against a grey brick wall, looking at tablets, phones and a laptop">
    <h1 class="hero-title">We are your partner for product management<br>and development!</h1>
  </section>

  <section class="you">
    <h2 class="you-heading">You ...</h2>

    <div class="question" style="top:88px">
      <svg class="question-icon" viewBox="0 0 84 88" aria-hidden="true">
        <ellipse cx="42" cy="83" rx="32" ry="3" fill="#cfcfcf"/>
        <circle cx="42" cy="42" r="38" fill="var(--blue)"/>
        <circle cx="42" cy="42" r="30" fill="#3fb1e6"/>
        <path d="M42 23a12 12 0 0 0-7 22v5h14v-5a12 12 0 0 0-7-22z" fill="#fff"/>
        <rect x="36" y="53" width="12" height="3" rx="1.5" fill="#fff"/>
        <rect x="37" y="58" width="10" height="3" rx="1.5" fill="#fff"/>
      </svg>
      <p class="question-text">have a digital<br>business idea?</p>
    </div>

    <div class="question" style="top:185px">
      <svg class="question-icon" viewBox="0 0 84 88" aria-hidden="true">
        <ellipse cx="42" cy="83" rx="32" ry="3" fill="#cfcfcf"/>
        <circle cx="42" cy="42" r="38" fill="var(--blue)"/>
        <circle cx="42" cy="42" r="30" fill="#3fb1e6"/>
        <rect x="22" y="29" width="40" height="27" rx="5" fill="#fff"/>
        <rect x="22" y="36" width="40" height="5" fill="var(--blue)"/>
        <rect x="27" y="46" width="18" height="4" rx="2" fill="var(--blue)"/>
      </svg>
      <p class="question-text">already obtained<br>a funding?</p>
    </div>

    <div class="question" style="top:285px">
      <svg class="question-icon" viewBox="0 0 84 88" aria-hidden="true">
        <ellipse cx="42" cy="83" rx="32" ry="3" fill="#cfcfcf"/>
        <circle cx="42" cy="42" r="38" fill="var(--blue)"/>
        <circle cx="42" cy="42" r="30" fill="#3fb1e6"/>
        <circle cx="28" cy="34" r="5" fill="#fff"/>
        <circle cx="56" cy="34" r="5" fill="#fff"/>
        <circle cx="42" cy="31" r="6" fill="#fff"/>
        <path d="M19 52a9 8 0 0 1 18 0z M47 52a9 8 0 0 1 18 0z" fill="#fff"/>
        <path d="M31 55a11 10 0 0 1 22 0z" fill="#fff"/>
        <rect x="20" y="55" width="44" height="3" rx="1.5" fill="#fff"/>
      </svg>
      <p class="question-text">are looking for experienced<br>support for product<br>development?</p>
    </div>
  </section>

  <section class="contact">
    <h3 class="contact-heading">HOW TO CONTACT US?</h3>
    <div class="person">
      <p>Malte Grunewald</p>
      <p>Agile Product Manager</p>
      <p class="person-line"><svg viewBox="0 0 12 12" aria-hidden="true"><path d="M2 1l2.5 0 1 3-1.5 1a7 7 0 0 0 3 3l1-1.5 3 1v2.5a1 1 0 0 1-1 1A10 10 0 0 1 1 2a1 1 0 0 1 1-1z" fill="var(--blue)"/></svg>+49-170-12 34 56 78</p>
      <p class="person-line"><svg viewBox="0 0 12 12" aria-hidden="true"><rect x="0.5" y="2" width="11" height="8" fill="var(--blue)"/><path d="M0.5 2.5l5.5 4 5.5-4" stroke="#fff" fill="none"/></svg>contact@grunewald-consult.de</p>
    </div>
    <div class="person">
      <p>Timo Basler</p>
      <p>Scrum Master, Dev-Lead</p>
      <p class="person-line"><svg viewBox="0 0 12 12" aria-hidden="true"><path d="M2 1l2.5 0 1 3-1.5 1a7 7 0 0 0 3 3l1-1.5 3 1v2.5a1 1 0 0 1-1 1A10 10 0 0 1 1 2a1 1 0 0 1 1-1z" fill="var(--blue)"/></svg>+49-171-9 87 65 43</p>
      <p class="person-line"><svg viewBox="0 0 12 12" aria-hidden="true"><rect x="0.5" y="2" width="11" height="8" fill="var(--blue)"/><path d="M0.5 2.5l5.5 4 5.5-4" stroke="#fff" fill="none"/></svg>timo.basler@nordlicht-dev.com</p>
    </div>
  </section>

  <footer class="site-band"><span class="site-url">www.grunewald-consult.de</span></footer>

  <section class="offer" aria-label="Services"></section>

  <h2 class="section-head" style="top:433px">We …</h2>
  <p class="item" style="top:519px"><svg viewBox="0 0 15 15" aria-hidden="true"><rect x="1" y="2" width="11" height="11" rx="1" fill="none" stroke="var(--blue)" stroke-width="1.5"/><path d="M4 7l3 3 7-8" fill="none" stroke="var(--blue)" stroke-width="1.8"/></svg>take over interim roles as: Product Owner, Scrum Master,<br>and Dev-Lead</p>
  <p class="item" style="top:560px"><svg viewBox="0 0 15 15" aria-hidden="true"><rect x="1" y="2" width="11" height="11" rx="1" fill="none" stroke="var(--blue)" stroke-width="1.5"/><path d="M4 7l3 3 7-8" fill="none" stroke="var(--blue)" stroke-width="1.8"/></svg>create your development team, optionally with<br>offshore/nearshore locations</p>
  <p class="item" style="top:599px"><svg viewBox="0 0 15 15" aria-hidden="true"><rect x="1" y="2" width="11" height="11" rx="1" fill="none" stroke="var(--blue)" stroke-width="1.5"/><path d="M4 7l3 3 7-8" fill="none" stroke="var(--blue)" stroke-width="1.8"/></svg>setup the cloud environment for your solution and<br>support its operations</p>
  <p class="item" style="top:639px"><svg viewBox="0 0 15 15" aria-hidden="true"><rect x="1" y="2" width="11" height="11" rx="1" fill="none" stroke="var(--blue)" stroke-width="1.5"/><path d="M4 7l3 3 7-8" fill="none" stroke="var(--blue)" stroke-width="1.8"/></svg>jointly establish an agile/lean mindset including<br>corresponding procedures</p>

  <h2 class="section-head" style="top:676px">If wanted, …</h2>
  <p class="item" style="top:761px"><svg viewBox="0 0 15 15" aria-hidden="true"><rect x="1" y="2" width="11" height="11" rx="1" fill="none" stroke="var(--blue)" stroke-width="1.5"/><path d="M4 7l3 3 7-8" fill="none" stroke="var(--blue)" stroke-width="1.8"/></svg>together we evolve your strategic orientation</p>
  <p class="item" style="top:786px"><svg viewBox="0 0 15 15" aria-hidden="true"><rect x="1" y="2" width="11" height="11" rx="1" fill="none" stroke="var(--blue)" stroke-width="1.5"/><path d="M4 7l3 3 7-8" fill="none" stroke="var(--blue)" stroke-width="1.8"/></svg>support you in architecture and technology design</p>
  <p class="item" style="top:810px"><svg viewBox="0 0 15 15" aria-hidden="true"><rect x="1" y="2" width="11" height="11" rx="1" fill="none" stroke="var(--blue)" stroke-width="1.5"/><path d="M4 7l3 3 7-8" fill="none" stroke="var(--blue)" stroke-width="1.8"/></svg>train you in product management and in creating a<br>scalable agile organisation</p>

  <h2 class="section-head" style="top:848px">Your benefits...</h2>
  <p class="item" style="top:933px"><svg viewBox="0 0 15 15" aria-hidden="true"><rect x="1" y="2" width="11" height="11" rx="1" fill="none" stroke="var(--blue)" stroke-width="1.5"/><path d="M4 7l3 3 7-8" fill="none" stroke="var(--blue)" stroke-width="1.8"/></svg>You focus on your ideas and your business model</p>
  <p class="item" style="top:958px"><svg viewBox="0 0 15 15" aria-hidden="true"><rect x="1" y="2" width="11" height="11" rx="1" fill="none" stroke="var(--blue)" stroke-width="1.5"/><path d="M4 7l3 3 7-8" fill="none" stroke="var(--blue)" stroke-width="1.8"/></svg>You receive a professional realization of your ideas –<br>in quality, time and budget</p>
  <p class="item" style="top:998px"><svg viewBox="0 0 15 15" aria-hidden="true"><rect x="1" y="2" width="11" height="11" rx="1" fill="none" stroke="var(--blue)" stroke-width="1.5"/><path d="M4 7l3 3 7-8" fill="none" stroke="var(--blue)" stroke-width="1.8"/></svg>Our lean/agile mindset supports your start-up mentality<br>and your commercial success</p>

  <h2 class="section-head" style="top:1037px">Why us?</h2>
  <p class="item" style="top:1124px"><svg viewBox="0 0 15 15" aria-hidden="true"><rect x="1" y="2" width="11" height="11" rx="1" fill="none" stroke="var(--blue)" stroke-width="1.5"/><path d="M4 7l3 3 7-8" fill="none" stroke="var(--blue)" stroke-width="1.8"/></svg>Combined expertise in product management, development,<br>and operations</p>
  <p class="item" style="top:1164px"><svg viewBox="0 0 15 15" aria-hidden="true"><rect x="1" y="2" width="11" height="11" rx="1" fill="none" stroke="var(--blue)" stroke-width="1.5"/><path d="M4 7l3 3 7-8" fill="none" stroke="var(--blue)" stroke-width="1.8"/></svg>Founders with experiences in digital business models and<br>numerous industries</p>

</main>
</body>
</html>
```